Veltora Solar business cards for gerald pashwick

Need a solar business card designed. I sell solar systems to home owners. Company’s name is Veltora solar. I want the business card to have this.
Veltora Solar
Gerald Pashwick
210.555.0147
Solar consultant
Gpashwick@veltorasolar.example
I would like the card to be black and green with the veltora logo on it if possible. If it’s possible to make atleast one of the designs green background with black lettering I would like to see that.
No upfront cost! Start saving today!
Target Market(s)
Residential home owners
Industry/Entity Type
Solar Energy
Contact Information for Business Card
Veltora Solar
Gerald Pashwick
210.555.0147
Solar consultant
Gpashwick@veltorasolar.example
Also if it would look better by adding in one of these that would be fine.

```html
<!DOCTYPE html>
<html lang="en">
<head>
<meta charset="utf-8">
<title>Veltora Solar – Business Cards</title>
<link rel="stylesheet" href="https://fonts.googleapis.com/css2?family=Montserrat:wght@700&family=Questrial&display=swap">
<style>
  :root {
    --stage: #2b2b2e;
    --green: #62dc48;
    --green-soft: #6fe057;
    --black: #050505;
    --ink: #0a0a0a;
  }
  * { box-sizing: border-box; margin: 0; padding: 0; }
  html, body {
    width: 1200px;
    height: 800px;
    overflow: hidden;
    background: var(--stage);
  }
  .stage {
    position: relative;
    width: 1200px;
    height: 800px;
    display: flex;
    align-items: center;
    justify-content: center;
    gap: 40px;
  }
  .card {
    position: relative;
    width: 540px;
    height: 309px;
    overflow: hidden;
    border-radius: 4px;
    box-shadow: 0 18px 40px rgba(0,0,0,0.45);
  }

  /* Front */
  .card--front {
    background: var(--green);
    color: var(--ink);
    display: flex;
    flex-direction: column;
    align-items: center;
    justify-content: center;
  }
  .front-wordmark {
    display: flex;
    align-items: center;
    gap: 14px;
  }
  .front-wordmark .mark-square {
    width: 22px;
    height: 22px;
    background: var(--ink);
  }
  .front-wordmark .brand-name {
    font-family: "Questrial", sans-serif;
    font-size: 48px;
    letter-spacing: 1px;
    text-transform: uppercase;
    line-height: 1;
  }
  .front-url {
    margin-top: 46px;
    font-family: "Questrial", sans-serif;
    font-size: 13px;
    letter-spacing: 3px;
  }

  /* Back */
  .card--back {
    background: var(--black);
    color: var(--green);
  }
  .back-band {
    position: absolute;
    inset: 0;
    width: 100%;
    height: 100%;
  }
  .back-info {
    position: absolute;
    left: 40px;
    bottom: 40px;
    width: 260px;
    font-family: "Questrial", sans-serif;
  }
  .back-brand {
    font-size: 34px;
    line-height: 0.95;
    text-transform: uppercase;
    letter-spacing: 0.5px;
  }
  .back-brand span { display: block; }
  .back-brand .brand-line-2 { padding-left: 46px; }
  .back-rule {
    margin: 12px 0 12px 10px;
    width: 190px;
    height: 1px;
    background: var(--green);
  }
  .person-name {
    font-family: "Montserrat", sans-serif;
    font-weight: 700;
    font-size: 15px;
    text-transform: uppercase;
    letter-spacing: 0.3px;
    padding-left: 10px;
  }
  .person-title {
    font-size: 15px;
    padding-left: 28px;
    margin-top: 2px;
  }
  .contact {
    list-style: none;
    margin-top: 14px;
    padding-left: 10px;
    font-size: 13px;
    line-height: 1.55;
  }
  .contact .phone { padding-left: 40px; }
</style>
</head>
<body>
<main class="stage">
  <section class="card card--front" aria-label="Business card front">
    <div class="front-wordmark">
      <span class="mark-square" aria-hidden="true"></span>
      <span class="brand-name">Veltora Solar</span>
    </div>
    <p class="front-url">www.veltorasolar.example</p>
  </section>

  <section class="card card--back" aria-label="Business card back">
    <svg class="back-band" viewBox="0 0 540 309" preserveAspectRatio="none" aria-hidden="true">
      <polygon points="330,0 380,0 430,309 395,309" fill="var(--green)"/>
      <polygon points="500,309 540,240 540,309" fill="var(--green)"/>
    </svg>
    <div class="back-info">
      <h1 class="back-brand"><span>Veltora</span><span class="brand-line-2">Solar</span></h1>
      <div class="back-rule"></div>
      <p class="person-name">Gerald Pashwick</p>
      <p class="person-title">Solar consultant</p>
      <ul class="contact">
        <li class="phone">210.555.0147</li>
        <li class="email">Gpashwick@veltorasolar.example</li>
      </ul>
    </div>
  </section>
</main>
</body>
</html>
```